Vital Spark Electrical in need of a business card design

We need a new business card designed for our electrical business. We have a logo already which I will attach below.
Would like the business card to be..
-BLACK background preferably, possibly white back ground behind logo if colours clash.
-White & Blue (logo blue) text
Something that makes the logo pop, & a modern look. Possibly minimal clean format.

REQUIRE:
-Logo on front & back

TEXT TO INCLUDE (ON ONE SIDE):

Tom Harlow
Director/Electrician
M: 0417 365 208
E:info@vitalsparkelectrical-example.com.au
W:www.vitalsparkelectrical-example.com.au
R.E.C 57318

Custom/New Homes
Renovations
Commercial Office/Shop Fit-outs
Communications & Security Cameras
Electric Vehicle Chargers
Airconditioning
Updates

Requirements
Nice to have
• Possibly even lighten the grey shades for the words 'Vital' & 'Spark' to be more easily read on a black background.

```html
<!DOCTYPE html>
<html lang="en">
<head>
<meta charset="utf-8">
<title>Vital Spark Electrical – Business Card</title>
<link href="https://fonts.googleapis.com/css2?family=Montserrat:wght@400;500;600;700&display=swap" rel="stylesheet">
<style>
  :root {
    --ink: #181818;
    --blue: #0598d8;
    --paper: #e6e6e6;
    --page: #f4f4f4;
    --grey-text: #666666;
    --rule: #b9b9b9;
    --white: #ffffff;
  }
  * { margin: 0; padding: 0; box-sizing: border-box; }
  html, body {
    width: 1200px; height: 1199px; overflow: hidden;
    background: var(--page);
    font-family: "Montserrat", sans-serif;
  }
  .card {
    position: absolute; left: 210px;
    width: 781px; height: 446px; overflow: hidden;
  }
  .card-front { top: 98px; }
  .card-back { top: 636px; }
  .card-shapes { position: absolute; inset: 0; }
  .wordmark {
    position: absolute; display: flex; align-items: center; gap: 12px;
    color: var(--white); font-weight: 600; white-space: nowrap;
  }
  .wordmark-dot { border-radius: 50%; background: var(--blue); flex: none; }
  .front-wordmark { left: 0; right: 0; top: 172px; justify-content: center; font-size: 34px; }
  .front-wordmark .wordmark-dot { width: 26px; height: 26px; }
  .front-url {
    position: absolute; left: 0; right: 0; top: 388px; text-align: center;
    font-size: 21px; font-weight: 500; color: var(--ink); letter-spacing: 0.2px;
  }
  .back-wordmark { left: 60px; top: 122px; font-size: 19px; gap: 9px; }
  .back-wordmark .wordmark-dot { width: 16px; height: 16px; }
  .services { position: absolute; left: 82px; top: 214px; list-style: none; }
  .services li {
    position: relative; padding-left: 20px; height: 26px;
    color: var(--white); font-size: 13.5px; font-weight: 500; line-height: 18px;
  }
  .services li::before {
    content: ""; position: absolute; left: 2px; top: 5px;
    width: 8px; height: 8px; border-radius: 50%; background: var(--blue);
  }
  .person-name {
    position: absolute; right: 79px; top: 104px;
    color: var(--blue); font-size: 30px; font-weight: 700; letter-spacing: 0.5px;
  }
  .person-role {
    position: absolute; right: 79px; top: 148px;
    color: var(--grey-text); font-size: 20px; font-weight: 500;
  }
  .contact {
    position: absolute; left: 513px; color: var(--grey-text);
    font-size: 13px; font-weight: 500; line-height: 17px;
  }
  .contact-phone { top: 216px; }
  .contact-licence { top: 275px; }
  .contact-web { top: 330px; }
</style>
</head>
<body>

<section class="card card-front" aria-label="Card front">
  <svg class="card-shapes" width="781" height="446" viewBox="0 0 781 446">
    <rect width="781" height="446" fill="var(--ink)"/>
    <path d="M0 360 H333 Q343 360 346 350 A47 47 0 0 1 434 350 Q437 360 447 360 H781 V446 H0 Z" fill="var(--blue)"/>
    <g class="globe-icon" fill="none" stroke="#222" stroke-width="2">
      <circle cx="390" cy="359" r="18"/>
      <ellipse cx="390" cy="359" rx="8" ry="18"/>
      <line x1="372" y1="359" x2="408" y2="359"/>
      <line x1="390" y1="341" x2="390" y2="377"/>
      <path d="M375 349 H405 M375 369 H405"/>
    </g>
  </svg>
  <div class="wordmark front-wordmark"><span class="wordmark-dot"></span>Vital Spark Electrical</div>
  <p class="front-url">www.vitalsparkelectrical-example.com.au</p>
</section>

<section class="card card-back" aria-label="Card back">
  <svg class="card-shapes" width="781" height="446" viewBox="0 0 781 446">
    <rect width="781" height="446" fill="var(--paper)"/>
    <rect width="361" height="446" fill="var(--ink)"/>
    <path d="M361 80 Q361 96 346 100 A49 49 0 0 0 346 186 Q361 190 361 206 Z" fill="var(--paper)"/>
    <circle cx="361" cy="143" r="35" fill="var(--blue)" role="img" aria-label="Profile icon"/>
    <line x1="397" y1="143" x2="702" y2="143" stroke="var(--rule)" stroke-width="2"/>
    <line x1="466" y1="225" x2="466" y2="343" stroke="var(--blue)" stroke-width="5"/>
    <circle cx="466" cy="225" r="20" fill="var(--blue)"/>
    <circle cx="466" cy="284" r="20" fill="var(--blue)"/>
    <circle cx="466" cy="343" r="20" fill="var(--blue)"/>
    <g fill="none" stroke="var(--white)" stroke-width="1.4">
      <rect x="459" y="213" width="14" height="24" rx="2.5"/>
      <line x1="459" y1="217" x2="473" y2="217"/>
      <line x1="459" y1="233" x2="473" y2="233"/>
      <path d="M466 296 C458 287 457 284 457 281 A9 9 0 0 1 475 281 C475 284 474 287 466 296 Z"/>
      <circle cx="466" cy="281" r="3"/>
      <path d="M457 352 L474 335 M466 335 H474 V343"/>
    </g>
    <line x1="513" y1="254" x2="702" y2="254" stroke="var(--rule)" stroke-width="1.5"/>
    <line x1="513" y1="316" x2="702" y2="316" stroke="var(--rule)" stroke-width="1.5"/>
  </svg>

  <div class="wordmark back-wordmark"><span class="wordmark-dot"></span>Vital Spark Electrical</div>

  <ul class="services">
    <li>Custom/New Homes</li>
    <li>Renovations</li>
    <li>Commercial Office/Shop Fit-outs</li>
    <li>Communications &amp; Security Cameras</li>
    <li>Electric Vehicle Chargers</li>
    <li>Airconditioning</li>
  </ul>

  <h1 class="person-name">TOM HARLOW</h1>
  <p class="person-role">Director/Electrician</p>

  <p class="contact contact-phone">0417 365 208</p>
  <p class="contact contact-licence">R.E.C 57318</p>
  <p class="contact contact-web">info@vitalsparkelectrical-example.com.au<br>www.vitalsparkelectrical-example.com.au</p>
</section>

</body>
</html>
```